Wine Shop Banners

Banner graphic/images required
Require banner images to match the present online wine shop.

www.kelterhaus-traube.de

The wine-shop presently has a very clean, simple design, lots of white space, which is very much the trend at the moment.

Requirements
Images or graphic design for present banners visible on the homepage

The colour and feeling of the banners must fit in with the present clean, simple design.

Work required
3 large slide-card/banners (can be more) and 3 smaller fixed banners below. Please view website to see present position of banners.

LARGE BANNERS x 3

Something special with white background within the banner space
White background on each slide-card. Small individual graphic image in the middle of the slide card. This could be either a simple element of wine:
ingredients, fruit (grape), bottle, cork, old bottle label etc. just displaying one item on each slide-card. Preferably with high quality graphic features.

Note:
We are trying the steer away from the classic stereotype wineshop design. The image/s should have a higher, individual graphic touch, which gives the design something different. Sometimes such artistic work is displayed in steampunk or even in nostalgic design, which leaves the viewer slightly memorized with the content.
To clarify: we are not looking for a full steampunk design but possibly certain elements of this will give you an idea what we mean. That is to say, the design can go slightly in this direction without going over the top. Something small but very eye-catching.

SMALLER BANNERS x 3

One idea is:
Showing a symbol e.g. - discount sign "%" against a white background but again with a high graphic quality.

Target Market(s)

People interested in purchasing wine.
Ages approx. 25 to 65

Industry/Entity Type

Shop

Requirements
Must have
• Something special with white background
• Small individual graphic image in the middle of the slide card.
Nice to have
• The image/s should have a higher, individual graphic touch, which gives the design something different. Something that leaves the viewer slightly memorized with the content.
Should not have
• Not the typical classical design that is often seen on wine shops.

```html
<!DOCTYPE html>
<html lang="de">
<head>
<meta charset="utf-8">
<title>Spesial Ofer – Banner</title>
<link rel="stylesheet" href="https://fonts.googleapis.com/css2?family=Great+Vibes&family=Playfair+Display:wght@400&display=swap">
<style>
  :root {
    --paper: #ffffff;
    --gold-deep: #b8792b;
    --gold-mid: #d9a352;
    --gold-light: #f1d08c;
    --gold-shine: #fbeed3;
    --gold-edge: #7a4a1c;
    --gold-flat: #bea36a;
  }
  html, body {
    margin: 0;
    padding: 0;
    overflow: hidden;
    background: var(--paper);
  }
  .banner {
    width: 1200px;
    height: 561px;
    position: relative;
    overflow: hidden;
    background: var(--paper);
  }
  .banner__art {
    position: absolute;
    inset: 0;
    width: 1200px;
    height: 561px;
  }
  .headline-script {
    font-family: "Great Vibes", cursive;
    font-size: 200px;
    fill: url(#goldSheen);
    stroke: var(--gold-edge);
    stroke-width: 1.2;
  }
  .headline-serif {
    font-family: "Playfair Display", serif;
    font-size: 285px;
    fill: var(--gold-flat);
  }
  .badge__edge { fill: none; stroke: var(--gold-edge); stroke-width: 13; }
  .badge__ring { fill: none; stroke: url(#goldRing); stroke-width: 10; }
  .percent__edge { fill: none; stroke: var(--gold-edge); stroke-width: 24; stroke-linecap: round; }
  .percent__body { fill: none; stroke: url(#goldSheen); stroke-width: 20; stroke-linecap: round; }
</style>
</head>
<body>
<div class="banner">
  <svg class="banner__art" viewBox="0 0 1200 561" xmlns="http://www.w3.org/2000/svg">
    <defs>
      <linearGradient id="goldSheen" x1="0" y1="0" x2="1" y2="1">
        <stop offset="0" stop-color="var(--gold-mid)"/>
        <stop offset="0.35" stop-color="var(--gold-light)"/>
        <stop offset="0.55" stop-color="var(--gold-shine)"/>
        <stop offset="0.8" stop-color="var(--gold-mid)"/>
        <stop offset="1" stop-color="var(--gold-deep)"/>
      </linearGradient>
      <linearGradient id="goldRing" gradientUnits="userSpaceOnUse" x1="-260" y1="-260" x2="260" y2="260">
        <stop offset="0" stop-color="var(--gold-light)"/>
        <stop offset="0.4" stop-color="var(--gold-shine)"/>
        <stop offset="0.7" stop-color="var(--gold-mid)"/>
        <stop offset="1" stop-color="var(--gold-deep)"/>
      </linearGradient>
      <path id="waveSegment" d="M250 0 Q269 23.5 246.2 43.4 Q222.2 59.5 234.9 85.5"/>
      <g id="waveEdge" class="badge__edge">
        <use href="#waveSegment"/><use href="#waveSegment" transform="rotate(20)"/><use href="#waveSegment" transform="rotate(40)"/>
        <use href="#waveSegment" transform="rotate(60)"/><use href="#waveSegment" transform="rotate(80)"/><use href="#waveSegment" transform="rotate(100)"/>
        <use href="#waveSegment" transform="rotate(120)"/><use href="#waveSegment" transform="rotate(140)"/><use href="#waveSegment" transform="rotate(160)"/>
        <use href="#waveSegment" transform="rotate(180)"/><use href="#waveSegment" transform="rotate(200)"/><use href="#waveSegment" transform="rotate(220)"/>
        <use href="#waveSegment" transform="rotate(240)"/><use href="#waveSegment" transform="rotate(260)"/><use href="#waveSegment" transform="rotate(280)"/>
        <use href="#waveSegment" transform="rotate(300)"/><use href="#waveSegment" transform="rotate(320)"/><use href="#waveSegment" transform="rotate(340)"/>
      </g>
    </defs>

    <g class="headline">
      <text class="headline-script" x="52" y="232" textLength="655" lengthAdjust="spacingAndGlyphs">Spesial</text>
      <text class="headline-serif" x="108" y="511" textLength="578" lengthAdjust="spacingAndGlyphs">OFER</text>
    </g>

    <g class="badge" transform="translate(1022 279)">
      <use href="#waveEdge"/>
      <use href="#waveEdge" class="badge__ring" style="stroke:url(#goldRing);stroke-width:9"/>
    </g>

    <g class="percent">
      <rect class="percent__edge" x="922" y="173" width="69" height="107" rx="34"/>
      <rect class="percent__body" x="922" y="173" width="69" height="107" rx="34"/>
      <line class="percent__edge" x1="1092" y1="160" x2="964" y2="410"/>
      <line class="percent__body" x1="1092" y1="160" x2="964" y2="410"/>
      <rect class="percent__edge" x="1073" y="289" width="67" height="113" rx="33"/>
      <rect class="percent__body" x="1073" y="289" width="67" height="113" rx="33"/>
    </g>
  </svg>
</div>
</body>
</html>
```